Medical business needs responsive Bootstrap theme design

We need a responsive Twitter Bootstrap theme for a hair transplant business in South Korea which looks good from full size desktop screens down to smartphone displays. We would like the site to match in style with our brochure design (see the PDF and Adobe Illustrator files), although it does not need to match exactly. Please feel free to use the design elements and images in the brochure. The general flow of the theme is shown in the wireframe image.
We expect graphic design, images, CSS, and HTML. No PHP/backend/ecommerce integration is expected.
Here are the links to the 3 stock images in the brochure:
http://www.pixelvaultimages.com/pic.mhtml?id=581927364
http://www.framequarry.com/photo/hair-transplant-gm738261945-61937482
http://www.framequarry.com/photo/doctor-inspecting-skin-of-head-gm749362817-62847193
You can use the Bootstrap template here as a starting point: http://quicklayoutkit.com/template-overviews/agency/
Our primary customers will be Westerners aged 28-45
Plastic Surgery
1 page

```html
<!DOCTYPE html>
<html lang="en">
<head>
<meta charset="utf-8">
<title>Hanbit Hair Clinic</title>
<link href="https://fonts.googleapis.com/css2?family=Roboto+Condensed:ital,wght@0,400;0,700;1,400;1,700&family=Open+Sans:wght@400;600&family=Playfair+Display:ital,wght@1,700&display=swap" rel="stylesheet">
<style>
:root{
  --blue:#3f86c6;
  --blue-dark:#2f6fab;
  --blue-light:#e3ecf5;
  --ink:#1c1c1c;
  --text:#555;
  --grey:#efefef;
  --white:#fff;
  --black:#0c0c0c;
}
*{box-sizing:border-box;margin:0;padding:0}
html,body{width:1200px;height:5143px;overflow:hidden}
body{font-family:"Open Sans",Arial,sans-serif;color:var(--text);position:relative;background:var(--white)}
section,header,footer,nav{position:absolute;left:0;width:1200px;overflow:hidden}
.abs{position:absolute;z-index:2}
.heading{font-family:"Roboto Condensed",Arial,sans-serif;font-weight:700;text-transform:uppercase}
.photo{position:absolute;z-index:1}

/* header */
.site-header{top:0;height:652px;background:linear-gradient(180deg,#f7f9fc 0%,#e6edf5 60%,#d9e3ee 100%)}
.site-header .photo-bg{inset:0;z-index:0;background:linear-gradient(100deg,#f3f6fa 0%,#e1e8f0 45%,#c9d6e3 100%)}
.site-header .photo-man{left:860px;top:290px;width:340px;height:362px;background:radial-gradient(ellipse at 50% 45%,#d9b59a 0%,#b58e74 45%,#8a6a58 80%,rgba(138,106,88,0) 100%)}
.top-contact{top:22px;left:705px;display:flex;gap:40px;font-size:15px;color:var(--ink)}
.top-contact span{display:flex;align-items:center;gap:10px}
.top-contact .ic{width:34px;height:34px;border-radius:50%;background:var(--ink);display:flex;align-items:center;justify-content:center}
.brand{top:190px;left:0;width:1200px;display:flex;justify-content:center;align-items:center;gap:14px}
.brand-dot{width:60px;height:60px;border-radius:50%;background:var(--blue)}
.brand-name{font-family:"Open Sans",Arial,sans-serif;font-weight:600;font-size:26px;color:var(--blue-dark)}
.tagline{top:325px;left:0;width:1200px;text-align:center;font-family:"Playfair Display",Georgia,serif;font-style:italic;font-weight:700;font-size:42px;color:var(--blue)}
.tagline-sub{top:385px;left:410px;width:380px;text-align:center;font-size:15px;line-height:22px;color:var(--blue)}

/* nav */
.main-nav{top:652px;height:58px;background:var(--blue)}
.main-nav ul{list-style:none;display:flex;position:absolute;left:290px;top:0;height:58px}
.main-nav li{font-family:"Roboto Condensed",Arial,sans-serif;font-size:15px;color:var(--white);text-transform:uppercase;line-height:58px;padding:0 36px}
.main-nav li.active{background:var(--black)}

/* about */
.about{top:710px;height:380px;background:var(--white)}
.about .photo-portrait{left:140px;top:20px;width:272px;height:360px;background:linear-gradient(180deg,#6a4a38 0%,#c89c80 40%,#e8c9b3 100%)}
.about h2{left:473px;top:50px;font-size:58px;color:var(--ink)}
.about h3{left:473px;top:120px;font-family:"Roboto Condensed",Arial,sans-serif;font-style:italic;font-size:30px;color:var(--blue);font-weight:400;text-transform:uppercase}
.about p{left:473px;top:175px;width:620px;font-size:16px;line-height:30px}
.about .more{left:473px;top:285px;font-family:"Roboto Condensed",Arial,sans-serif;font-style:italic;font-weight:700;font-size:17px;color:var(--ink);text-decoration:underline}

/* why */
.why{top:1090px;height:693px;background:var(--blue);color:var(--white)}
.why h2{left:0;width:1200px;top:62px;text-align:center;font-size:48px;color:var(--white)}
.why .photo-man2{left:730px;top:282px;width:470px;height:411px;background:linear-gradient(160deg,#5d86b5 0%,#c7a187 45%,#3a3a3a 100%)}
.feat-icon{border-radius:50%;background:var(--white);border:6px solid rgba(255,255,255,.45);background-clip:padding-box;display:flex;align-items:center;justify-content:center}
.feat h4{font-family:"Roboto Condensed",Arial,sans-serif;font-size:20px;text-transform:uppercase;margin-bottom:10px}
.feat p{font-size:14px;line-height:24px}

/* method */
.method{top:1783px;height:1070px;background:linear-gradient(180deg,#f4f4f4,#e9edf1)}
.method h2{left:0;width:1200px;top:60px;text-align:center;font-size:48px;color:var(--blue)}
.method .lead{left:400px;top:125px;width:400px;text-align:center;font-size:14px;line-height:24px;color:var(--blue)}
.method h3{font-family:"Roboto Condensed",Arial,sans-serif;font-style:italic;font-weight:700;font-size:23px;color:var(--blue-dark);left:82px}
.step-num{font-size:16px;color:var(--ink)}
.step-img{width:200px;height:200px;border-radius:50%;border:6px solid var(--white)}
.step-cap{width:330px;text-align:center;font-size:14px;line-height:24px}

/* comparison */
.compare{top:2853px;height:604px;background:var(--blue)}
.compare h2{left:0;width:1200px;top:60px;text-align:center;font-size:46px;color:var(--white);font-weight:400}
.compare .divider{left:599px;top:150px;width:2px;height:320px;background:rgba(255,255,255,.5)}
.card{background:var(--white);width:477px;height:322px}
.card .photo{left:14px;top:14px;width:449px;height:172px;background:linear-gradient(90deg,#d8b9a2,#a88570 50%,#3b2d26)}
.card h4{position:absolute;top:205px;width:100%;text-align:center;font-size:19px;color:var(--ink);font-weight:400}
.card p{position:absolute;top:240px;left:60px;width:357px;text-align:center;font-size:14px;line-height:24px}
.btn-show{left:551px;top:502px;width:98px;height:40px;background:var(--white);color:var(--blue);font-family:"Roboto Condensed",Arial,sans-serif;font-size:13px;text-transform:uppercase;text-align:center;line-height:40px}

/* blog */
.blog{top:3457px;height:607px;background:var(--white)}
.blog h2{left:0;width:1200px;top:60px;text-align:center;font-size:46px;color:var(--blue);font-weight:400}
.blog .lead{left:330px;top:125px;width:540px;text-align:center;font-size:15px;line-height:26px;color:var(--ink)}
.post{top:220px;width:309px;height:281px}
.post-1{left:79px;background:linear-gradient(160deg,#7fa9d6,#3f86c6)}
.post-1 .title{position:absolute;left:18px;top:28px;font-family:"Playfair Display",Georgia,serif;font-style:italic;font-size:22px;color:var(--white)}
.post-1 .date{position:absolute;left:18px;top:66px;font-size:13px;font-style:italic;color:var(--white)}
.post-1 p{position:absolute;left:18px;top:110px;width:230px;font-size:14px;line-height:24px;color:var(--white)}
.post-2{left:446px;background:linear-gradient(180deg,#eae5e0,#b08d78 55%,#6e5a4f)}
.post-3{left:813px;background:linear-gradient(180deg,#ffffff,#e5c9a8 45%,#b18d70)}
.dots{left:560px;top:525px;display:flex;gap:14px}
.dots i{width:14px;height:14px;border-radius:50%;border:2px solid var(--blue)}
.dots i.on{background:var(--blue)}

/* testimonials */
.testimonials{top:4064px;height:593px;background:linear-gradient(180deg,#dbe6f1,#c9d8e8)}
.testimonials h2{left:0;width:1200px;top:60px;text-align:center;font-size:46px;color:var(--blue);font-weight:400}
.testimonials .sub{left:0;width:1200px;top:117px;text-align:center;font-family:"Roboto Condensed",Arial,sans-serif;font-weight:700;font-size:16px;color:var(--ink)}
.quote{left:240px;top:196px;width:720px;height:182px;background:rgba(255,255,255,.85);border:1px solid #9aa9b8;padding:45px 90px;text-align:center;font-size:15px;line-height:26px}
.quote-tip{left:585px;top:377px}
.avatar{left:562px;top:414px;width:76px;height:76px;border-radius:50%;background:radial-gradient(circle,#d8b49a,#8a6a58);border:3px solid var(--white)}
.client{left:0;width:1200px;top:505px;text-align:center;font-family:"Roboto Condensed",Arial,sans-serif;font-size:15px;color:var(--ink);text-transform:uppercase}

/* contact */
.contact{top:4657px;height:418px;background:var(--blue)}
.contact h2{left:79px;top:55px;font-family:"Roboto Condensed",Arial,sans-serif;font-size:44px;color:var(--white);font-weight:700}
.field{left:79px;width:257px;height:40px;background:var(--white);font-size:14px;color:#888;padding:9px 12px}
.field-msg{left:350px;top:121px;width:240px;height:215px}
.btn-submit{left:79px;top:350px;width:100px;height:40px;background:var(--black);color:var(--white);font-size:14px;line-height:40px;text-align:center}
.map{left:600px;top:0;width:600px;height:418px;background:linear-gradient(135deg,#f1ecdf,#e8e2d1 50%,#dcd8c8)}
.map-info{left:172px;top:120px;width:223px;height:180px;background:var(--white);padding:16px 14px;font-size:13px;line-height:20px;color:var(--blue)}
.map-info div{display:flex;gap:12px;margin-bottom:14px;align-items:flex-start}
.map-info .ic{flex:0 0 30px;width:30px;height:30px;border-radius:50%;background:var(--blue);display:flex;align-items:center;justify-content:center}

/* footer */
.site-footer{top:5075px;height:68px;background:var(--black);color:var(--white);text-align:center;line-height:68px;font-size:14px}
.site-footer span{color:var(--blue);text-decoration:underline}
</style>
</head>
<body>

<header class="site-header">
  <div class="photo photo-bg" role="img" aria-label="Bright clinic treatment room with chairs"></div>
  <div class="photo photo-man" role="img" aria-label="Smiling man running his hand through thick hair"></div>
  <div class="abs top-contact">
    <span><span class="ic"><svg width="18" height="18" viewBox="0 0 24 24"><path fill="#fff" d="M6.6 10.8a15 15 0 0 0 6.6 6.6l2.2-2.2c.3-.3.7-.4 1-.2 1.1.4 2.3.6 3.6.6.6 0 1 .4 1 1V20c0 .6-.4 1-1 1A17 17 0 0 1 3 4c0-.6.4-1 1-1h3.5c.6 0 1 .4 1 1 0 1.3.2 2.5.6 3.6.1.3 0 .7-.2 1z"/></svg></span>0123 555 014</span>
    <span><span class="ic"><svg width="18" height="18" viewBox="0 0 24 24"><path fill="#fff" d="M3 6h18v12H3z"/><path d="M3 6l9 7 9-7" stroke="#1c1c1c" stroke-width="2" fill="none"/></svg></span>hello@hanbithair.example</span>
  </div>
  <div class="abs brand"><span class="brand-dot"></span><span class="brand-name">Hanbit Hair Clinic</span></div>
  <div class="abs tagline">Effective Hair Restoration</div>
  <p class="abs tagline-sub">Lorem ipsum dolor sit amet, consectetur adipiscing elit. Aenean feugiat dictum lacus. Lorem ipsum dolor si...</p>
</header>

<nav class="main-nav">
  <ul>
    <li class="active">Home</li><li>About</li><li>Method</li><li>Blog</li><li>Contact Us</li>
  </ul>
</nav>

<section class="about">
  <div class="photo photo-portrait" role="img" aria-label="Man in profile touching his chin"></div>
  <h2 class="abs heading">About</h2>
  <h3 class="abs">Hanbit Hair Clinic</h3>
  <p class="abs">Lorem ipsum dolor sit amet, consectetur adipiscing elit. Aenean feugiat dictum lacus. Lorem ipsum dolor sit amet, consectetur adipiscing elit. Lorem ipsum dolor sit amet, consectetur adipiscing elit. adipiscing elit.</p>
  <span class="abs more">READ MORE</span>
</section>

<section class="why">
  <h2 class="abs heading">Why South Korea?</h2>
  <svg class="abs" style="left:0;top:0" width="700" height="693"><path d="M172 300 C172 330 210 330 274 395 M274 460 C274 500 300 500 386 560" stroke="#fff" stroke-width="3" stroke-dasharray="3 9" stroke-linecap="round" fill="none"/></svg>
  <div class="abs feat-icon" style="left:103px;top:162px;width:137px;height:137px"><svg width="60" height="60" viewBox="0 0 24 24"><circle cx="12" cy="8" r="5" fill="#3f86c6"/><path d="M3 20c4-3 8-3 11-1l6-3" stroke="#3f86c6" stroke-width="2" fill="none"/></svg></div>
  <div class="abs feat" style="left:254px;top:188px;width:310px"><h4>Quality of Care</h4><p>Hair transplantation surgery has improved significantly over the last decade. State of the art technology ensures transplanted...</p></div>
  <div class="abs feat-icon" style="left:205px;top:323px;width:137px;height:137px"><svg width="60" height="60" viewBox="0 0 24 24"><rect x="3" y="7" width="18" height="10" rx="2" fill="#3f86c6"/><path d="M6 17v2M18 17v2" stroke="#3f86c6" stroke-width="2"/></svg></div>
  <div class="abs feat" style="left:353px;top:336px;width:320px"><h4>Convenience</h4><p>you are already in South Korea or Japan, the procedure can be done in one day with follow up appointments available on the request...</p></div>
  <div class="abs feat-icon" style="left:326px;top:495px;width:120px;height:120px"><svg width="54" height="54" viewBox="0 0 24 24"><circle cx="12" cy="10" r="6" fill="#3f86c6"/><path d="M3 20c4-3 8-3 11-1l6-3" stroke="#3f86c6" stroke-width="2" fill="none"/></svg></div>
  <div class="abs feat" style="left:473px;top:498px;width:240px"><h4>Cost Savings</h4><p>The average hair transplant surgery in South Korea costs about $5,000 to $6,000,30-40% less than if done in...</p></div>
  <div class="photo photo-man2" role="img" aria-label="Smiling man in a suit touching his hair"></div>
</section>

<section class="method">
  <h2 class="abs heading">Method</h2>
  <p class="abs lead">Lorem ipsum dolor sit amet, consectetur adipiscing elit. Aenean feugiat dictum lacus. Lorem ipsum dolor si...</p>
  <h3 class="abs" style="top:185px">Traditional follicular unit transplant</h3>
  <span class="abs step-num" style="left:82px;top:248px">1.</span>
  <span class="abs step-num" style="left:440px;top:248px">2.</span>
  <span class="abs step-num" style="left:796px;top:248px">3.</span>
  <div class="abs step-img" role="img" aria-label="Illustration of a strip of scalp removed from the back of the head" style="left:143px;top:247px;background:radial-gradient(circle,#e0a48a,#8f8f8f)"></div>
  <div class="abs step-img" role="img" aria-label="Illustration of the incision edges sutured together" style="left:503px;top:247px;background:radial-gradient(circle,#e9b39c,#c98e78)"></div>
  <div class="abs step-img" role="img" aria-label="Illustration of a healed fine scar hidden by hair" style="left:863px;top:247px;background:radial-gradient(circle,#d9b8a6,#6d4a3a)"></div>
  <p class="abs step-cap" style="left:78px;top:480px">Hair on back of head is trimmed and a narrow strip is surgically removed so that hair can grow through and camouflage the scar.</p>
  <p class="abs step-cap" style="left:438px;top:480px">The hair from abov and below the excision is gently brought together and sutured using advanced surgical closure techniques...</p>
  <p class="abs step-cap" style="left:798px;top:480px">When the wound is healed... a fine scar line is almost completely concealed by the surrounding hair...</p>
  <h3 class="abs" style="top:625px">Follicular Unit Extraction</h3>
  <span class="abs step-num" style="left:82px;top:687px">1.</span>
  <span class="abs step-num" style="left:440px;top:687px">2.</span>
  <span class="abs step-num" style="left:796px;top:687px">3.</span>
  <div class="abs step-img" role="img" aria-label="Illustration of individual follicles extracted from the donor area" style="left:143px;top:687px;background:radial-gradient(circle,#e9a98a,#8a8a8a)"></div>
  <div class="abs step-img" role="img" aria-label="Illustration of a single follicle placed into the scalp" style="left:503px;top:687px;background:radial-gradient(circle,#f4f4f4,#d8d8d8)"></div>
  <div class="abs step-img" role="img" aria-label="Illustration of the healed donor area with tiny dot scars" style="left:863px;top:687px;background:radial-gradient(circle,#e2b49a,#b88266)"></div>
  <p class="abs step-cap" style="left:78px;top:915px">Hair on back of head is trimmed and a narrow strip is surgically removed so that hair can grow through and camouflage the scar.</p>
  <p class="abs step-cap" style="left:438px;top:915px">The hair from abov and below the excision is gently brought together and sutured using advanced surgical closure techniques...</p>
  <p class="abs step-cap" style="left:798px;top:915px">When the wound is healed... a fine scar line is almost completely concealed by the surrounding hair...</p>
</section>

<section class="compare">
  <h2 class="abs heading">Comparision</h2>
  <div class="abs divider"></div>
  <div class="abs card" style="left:79px;top:152px">
    <div class="photo" role="img" aria-label="Before and after photos of a balding scalp"></div>
    <h4>After 8 Month Treatment</h4>
    <p>Lorem ipsum dolor sit amet, consectetur adipiscing elit. Aenean feugiat dictum lacusLorem ips...</p>
  </div>
  <div class="abs card" style="left:645px;top:152px">
    <div class="photo" role="img" aria-label="Before and after photos of a restored hairline"></div>
    <h4>After 6 Month Treatment</h4>
    <p>Lorem ipsum dolor sit amet, consectetur adipiscing elit. Aenean feugiat dictum lacusLorem ips...</p>
  </div>
  <div class="abs btn-show">Show All</div>
</section>

<section class="blog">
  <h2 class="abs heading">Blog</h2>
  <p class="abs lead">Lorem ipsum dolor sit amet, consectetur adipiscing elit. Aenean feugiat dictum Lorem ipsum lacus...</p>
  <div class="abs post post-1" role="img" aria-label="Blog post cover with a man's portrait under a blue overlay">
    <span class="title">Lorem ipsum</span>
    <span class="date">2<sup>nd</sup> January, 2016</span>
    <p>Lorem ipsum dolor sit amet, consectetur adipiscing elit. Aenean feugiat dictum lacus...</p>
  </div>
  <div class="abs post post-2" role="img" aria-label="Portrait of a shirtless man with short hair"></div>
  <div class="abs post post-3" role="img" aria-label="Portrait of a young man with styled blond hair"></div>
  <div class="abs dots"><i class="on"></i><i></i><i></i></div>
</section>

<section class="testimonials">
  <h2 class="abs heading">Testimonials</h2>
  <div class="abs sub">WHAT OUR CLIENT SAY</div>
  <div class="abs quote">Lorem ipsum dolor sit amet, consectetur adipiscing elit. Aenean feugiat dictum lacusLorem ipsum dolor sit amet, consectetur adipiscing elit. Aenean feugiat dictum lacus...</div>
  <svg class="abs quote-tip" width="30" height="18"><path d="M0 0 L15 17 L30 0" fill="#f5f7fa" stroke="#9aa9b8"/></svg>
  <div class="abs avatar" role="img" aria-label="Client portrait"></div>
  <div class="abs client">Client Name</div>
</section>

<section class="contact">
  <h2 class="abs">Contact</h2>
  <div class="abs field" style="top:121px">First Name*</div>
  <div class="abs field" style="top:180px">Email*</div>
  <div class="abs field" style="top:238px">Phone*</div>
  <div class="abs field" style="top:296px">Subject*</div>
  <div class="abs field field-msg">Message*</div>
  <div class="abs btn-submit">Submit</div>
  <div class="abs map" role="img" aria-label="Street map showing the clinic location">
    <div class="abs map-info">
      <div><span class="ic"><svg width="14" height="14" viewBox="0 0 24 24"><path fill="#fff" d="M12 2a7 7 0 0 0-7 7c0 5 7 13 7 13s7-8 7-13a7 7 0 0 0-7-7zm0 9.5a2.5 2.5 0 1 1 0-5 2.5 2.5 0 0 1 0 5z"/></svg></span><span>420 Maple Street, City, CA 90210, Korea</span></div>
      <div><span class="ic"><svg width="14" height="14" viewBox="0 0 24 24"><path fill="#fff" d="M3 6h18v12H3z"/></svg></span><span>hello@hanbithair.example</span></div>
      <div><span class="ic"><svg width="14" height="14" viewBox="0 0 24 24"><path fill="#fff" d="M6.6 10.8a15 15 0 0 0 6.6 6.6l2.2-2.2c.3-.3.7-.4 1-.2 1.1.4 2.3.6 3.6.6.6 0 1 .4 1 1V20c0 .6-.4 1-1 1A17 17 0 0 1 3 4c0-.6.4-1 1-1h3.5c.6 0 1 .4 1 1 0 1.3.2 2.5.6 3.6.1.3 0 .7-.2 1z"/></svg></span><span>0123 555 014</span></div>
    </div>
  </div>
</section>

<footer class="site-footer">© 2015 <span>HANBIT HAIR CLINIC</span> | Incorporated</footer>

</body>
</html>
```